Real Estate and Property Management Company needs new listings

We need a business card for our company, Dorsell Estates & Property Management. We maximize financial returns on residential investment properties. By evaluating the current value and health of a property, we devise a financial plan to rehabilitate the property while earning an income over a period of years for rental properties, or suggest meaningful updates and improvements to ensure maximum payout on sales properties.
We would like to see our business cards with the colors black and metallic burgundy. The final design should communicate management and financial growth.

Target Market(s)

Home Owners of single family, detatched residential homes.

Industry/Entity Type

Business

Contact Information for Business Card

Side 1: Maren Dorsell
Broker, Owner
Maren@DorsellEstates.example
555-284-7719 (Cell)
555-731-4062 (Office)
Please incorporate in the design of side 1 that we have been in business for 40 years, along with communicating sales and management.
Side 2: Tessa Dorsell
Property Manager
Tessa@DorsellEstates.example
555-284-7745 (Cell)
555-731-4062 (Office)
Please incorporate that we are a family owner and operated company on side 2.

Font styles to use
Serif

Requirements
Must have
• Elegant, feminine design of metallic burgundy on black on double sided card.
Nice to have
• I would like to see some consistency of design on the front and back of the card, with perhaps a bold, thick line of burgundy on the right, vertical side. I would also like the black card stock to have some geometrical design or texture.
Should not have
• Any of the colors provided below. I cannot choose burgundy, which is the color for our business. Is this the only color selection available?

```html
<!DOCTYPE html>
<html lang="en">
<head>
<meta charset="utf-8">
<title>Dorsell Estates – Business Cards</title>
<link rel="stylesheet" href="https://fonts.googleapis.com/css2?family=Lora:wght@400;600;700&display=swap">
<style>
  :root {
    --backdrop: #2b2b2b;
    --card-white: #f2f2f2;
    --card-black: #151515;
    --burgundy: #7a1a30;
    --burgundy-deep: #5e1124;
    --burgundy-light: #b0405c;
    --burgundy-sheen: #c9647c;
    --text-light: #f5f5f5;
  }
  html, body {
    margin: 0;
    width: 1200px;
    height: 834px;
    overflow: hidden;
    background: var(--backdrop);
    font-family: "Lora", serif;
  }
  .canvas { position: relative; width: 1200px; height: 834px; }
  .business-card {
    position: absolute;
    width: 540px;
    height: 310px;
    box-shadow: 0 10px 30px rgba(0,0,0,.45);
  }
  .card-owner { left: 90px; top: 80px; }
  .card-manager { left: 570px; top: 444px; }
  .business-card svg { display: block; width: 540px; height: 310px; }
  .panel-white { fill: var(--card-white); }
  .panel-black { fill: var(--card-black); }
  .band-lower { fill: var(--burgundy-deep); }
  .band-upper { fill: url(#burgundySheen); }
  .house-art { fill: url(#houseTone); }
  .brand-name { fill: var(--burgundy); font: 600 15px "Lora", serif; letter-spacing: .6px; }
  .person-name { fill: var(--text-light); font: 700 19px "Lora", serif; }
  .person-role { fill: var(--burgundy-sheen); font: 400 12px "Lora", serif; }
  .contact-line { fill: var(--text-light); font: 400 12px "Lora", serif; }
  .contact-icon { fill: none; stroke: var(--burgundy-sheen); stroke-width: 1.4; }
  .tagline { fill: var(--text-light); font: 600 9.5px "Lora", serif; letter-spacing: .2px; }
</style>
</head>
<body>
<div class="canvas">

  <svg width="0" height="0" style="position:absolute" aria-hidden="true">
    <defs>
      <linearGradient id="houseTone" x1="0" y1="0" x2="1" y2="1">
        <stop offset="0" stop-color="#bdbdbd"/>
        <stop offset="1" stop-color="#5a5a5a"/>
      </linearGradient>
      <linearGradient id="burgundySheen" x1="0" y1="0" x2="1" y2="0">
        <stop offset="0" stop-color="#8c2139"/>
        <stop offset=".5" stop-color="#b0405c"/>
        <stop offset="1" stop-color="#7a1a30"/>
      </linearGradient>
      <g id="cardBase">
        <rect class="panel-white" width="540" height="310"/>
        <path class="panel-black" d="M255 0 H540 V310 H250 V262 H255 V52 L243 44 L255 36 Z"/>
        <polygon class="band-lower" points="0,284 228,284 240,262 246,262 234,296 0,296"/>
        <polygon class="band-upper" points="240,260 540,260 540,282 228,282"/>
        <rect class="house-art" x="70" y="95" width="130" height="95" role="img" aria-label="Line drawing of a two-storey family house with chimney"/>
        <text class="brand-name" x="135" y="222" text-anchor="middle">DORSELL ESTATES</text>
      </g>
      <g id="iconSet">
        <rect class="contact-icon" x="0" y="-10" width="7" height="12" rx="1.5"/>
        <path class="contact-icon" d="M-1 14 q5 -5 10 0 v3 h-10 z"/>
        <circle class="contact-icon" cx="4" cy="34" r="5.5"/>
        <path class="contact-icon" d="M-1.5 34 h11 M4 28.5 v11"/>
      </g>
    </defs>
  </svg>

  <article class="business-card card-owner">
    <svg viewBox="0 0 540 310">
      <use href="#cardBase"/>
      <text class="person-name" x="300" y="82">Maren Dorsell</text>
      <text class="person-role" x="300" y="100">Broker, Owner</text>
      <use href="#iconSet" x="318" y="134"/>
      <text class="contact-line" x="338" y="135">555-284-7719</text>
      <text class="contact-line" x="338" y="153">555-731-4062</text>
      <text class="contact-line" x="338" y="172">Maren@DorsellEstates.example</text>
      <text class="tagline" x="252" y="275">WE HAVE BEEN IN BUSINESS FOR 40 YEARS</text>
    </svg>
  </article>

  <article class="business-card card-manager">
    <svg viewBox="0 0 540 310">
      <use href="#cardBase"/>
      <text class="person-name" x="300" y="82">Tessa Dorsell</text>
      <text class="person-role" x="300" y="100">Property Manager</text>
      <use href="#iconSet" x="318" y="134"/>
      <text class="contact-line" x="338" y="135">555-284-7745</text>
      <text class="contact-line" x="338" y="153">555-731-4062</text>
      <text class="contact-line" x="338" y="172">Tessa@DorsellEstates.example</text>
      <text class="tagline" x="252" y="275">WE ARE A FAMILY OWNER AND OPERATED COMPANY</text>
    </svg>
  </article>

</div>
</body>
</html>
```